Coffee House With Cycling Theme Wants Business Cards

We want to create a business card for a coffee house that has a cycling theme. We expect to use the current logo on one side of the business card and we have been considering adding the words 'COFFEE HOUSE' underneath (see example). For the other side of the business card we want an interesting design with tag-line, address and social media links (the normal business card stuff). See examples provided but we are not fixed on having it exactly as shown, we are very open to great creative ideas. Please note our logo has the initials ‘RM' in orange embedded in the design and this must be retained. However, you can play with the words COFFEE HOUSE as well as use the orange color on the backside of the business card, as you see fit. For an image on the backside of the business card it can be a photo, hand-drawn or whatever but it must visually combine coffee and cycling in some way. The interior of the Coffee House will be reclaimed wood, rustic and have an urban feel to it with cycling artifacts hanging from the walls/ceiling, etc. Finally, it would be beneficial if the business card design elements can be easily used on flyers and other promotional assets. Good luck, we are looking forward to seeing your creative ideas.

Target Market(s)

Coffee lovers and cycling fans

Contact Information for Business Card

See project description.

Colors

Designer to choose colors to be used in the design.

Requirements
Must have
• Must use the current logo provided and combine a coffee and bike theme.
Nice to have
• Orange is used in current logo and could be used as an accent color on the backside of the business card.

```html
<!DOCTYPE html>
<html lang="en">
<head>
<meta charset="utf-8">
<title>Coffee House Business Card</title>
<link href="https://fonts.googleapis.com/css2?family=Lato:wght@300;400&display=swap" rel="stylesheet">
<style>
  :root {
    --page: #ececec;
    --orange: #f26a2a;
    --white: #ffffff;
    --dark: #140f0d;
    --dark-warm: #2a1d18;
    --roast: #4a2a1f;
    --text-light: #e9e4e0;
  }
  html, body {
    margin: 0;
    width: 1200px;
    height: 1200px;
    overflow: hidden;
    background: var(--page);
    font-family: "Lato", sans-serif;
  }
  .card {
    position: absolute;
    left: 228px;
    width: 743px;
    height: 424px;
    overflow: hidden;
  }
  .card-front {
    top: 134px;
    background: var(--orange);
    text-align: center;
    color: var(--white);
  }
  .brand-mark {
    position: absolute;
    left: 0; right: 0;
    top: 110px;
    font-weight: 300;
    font-size: 120px;
    line-height: 1;
    letter-spacing: 6px;
  }
  .brand-name {
    position: absolute;
    left: 0; right: 0;
    top: 258px;
    font-weight: 300;
    font-size: 47px;
    letter-spacing: 1px;
  }
  .card-back {
    top: 619px;
    width: 739px;
    height: 422px;
    background: var(--dark);
    color: var(--text-light);
  }
  .photo-area {
    position: absolute;
    inset: 0;
    background: linear-gradient(100deg, var(--dark) 0%, var(--dark-warm) 50%, var(--roast) 75%, var(--dark-warm) 100%);
  }
  .back-title {
    position: absolute;
    left: 42px; top: 42px;
    margin: 0;
    font-weight: 400;
    font-size: 37.5px;
    line-height: 1.1;
    color: var(--white);
    letter-spacing: 0.3px;
  }
  .contact-list {
    position: absolute;
    left: 42px; top: 0;
    margin: 0; padding: 0;
    list-style: none;
    font-size: 12.5px;
  }
  .contact-item {
    position: absolute;
    left: 0;
    display: flex;
    align-items: center;
    white-space: nowrap;
  }
  .contact-icon {
    width: 18px; height: 18px;
    margin-right: 12px;
    color: var(--orange);
    display: flex; align-items: center; justify-content: center;
    font-size: 18px;
    line-height: 1;
  }
</style>
</head>
<body>

<section class="card card-front">
  <div class="brand-mark">RM</div>
  <div class="brand-name">COFFEE HOUSE</div>
</section>

<section class="card card-back">
  <div class="photo-area" role="img" aria-label="Photo of a cup of cappuccino with latte art on a dark table"></div>
  <h1 class="back-title">COFFEE HOUSE</h1>
  <ul class="contact-list">
    <li class="contact-item" style="top:136px">
      <span class="contact-icon"><svg width="12" height="17" viewBox="0 0 12 17"><path d="M6 0C2.7 0 0 2.6 0 5.9 0 10 6 17 6 17s6-7 6-11.1C12 2.6 9.3 0 6 0zm0 8.2a2.3 2.3 0 110-4.6 2.3 2.3 0 010 4.6z" fill="currentColor"/></svg></span>
      2740 Orchard Ave. Millbrook, NJ 07180
    </li>
    <li class="contact-item" style="top:170px">
      <span class="contact-icon"><svg width="16" height="16" viewBox="0 0 24 24"><path d="M6.6 10.8a15.1 15.1 0 006.6 6.6l2.2-2.2c.3-.3.7-.4 1-.2 1.1.4 2.3.6 3.6.6.6 0 1 .4 1 1V20c0 .6-.4 1-1 1A17 17 0 013 4c0-.6.4-1 1-1h3.5c.6 0 1 .4 1 1 0 1.3.2 2.5.6 3.6.1.3 0 .7-.2 1z" fill="currentColor"/></svg></span>
      (+014)&nbsp; 555 0182
    </li>
    <li class="contact-item" style="top:207px">
      <span class="contact-icon">@</span>
      info@cranksidecafe.com
    </li>
    <li class="contact-item" style="top:285px">
      <span class="contact-icon"><svg width="14" height="14" viewBox="0 0 14 14"><circle cx="7" cy="7" r="6" fill="none" stroke="currentColor" stroke-width="1.6"/></svg></span>
      Follow us /CranksideCafe
    </li>
    <li class="contact-item" style="top:321px">
      <span class="contact-icon"><svg width="14" height="14" viewBox="0 0 14 14"><circle cx="7" cy="7" r="6" fill="none" stroke="currentColor" stroke-width="1.6"/></svg></span>
      Photos /CranksideCafe
    </li>
    <li class="contact-item" style="top:359px">
      <span class="contact-icon"><svg width="18" height="18" viewBox="0 0 18 18" fill="none" stroke="currentColor" stroke-width="1.4"><circle cx="9" cy="9" r="7.5"/><ellipse cx="9" cy="9" rx="3.2" ry="7.5"/><path d="M1.5 9h15"/></svg></span>
      www.cranksidecafe.com
    </li>
  </ul>
</section>

</body>
</html>
```